Webdesign für Management Coaching
Zielgruppe
Ich bin Coach/biete Coaching-Leistungen an.
Zielgruppe: Fokus auf Führungskräfte/Entscheider/Management mit technischem Hintergrund (Forschung & Entwicklung, Engineering, Technik, Maschinenbau, Naturwissenschaften)
Coaching-Schwerpunkte: Sinn-Coaching, Begleitung bei Umbrüchen und Veränderungen (privat & beruflich), Sparring & Reflexion
Aufgabenstellung
Gewünscht wurde ein helles Design, das die Logo-Farben aufnimmt. Ausrichtung am Logo & den verwendeten Farben, Schriften
Bilder: Ich werde noch Fotos beim Fotografen machen, die eingebunden werden sollen (Profil, etc.). Bitte Anhaltspunkte nennen, worauf ich die Fotografin hinweisen soll/welche Motive ins Konzept passen.

```html
<!DOCTYPE html>
<html lang="de">
<head>
<meta charset="utf-8">
<title>Matthias Lindholm – Coaching für technische Führungskräfte</title>
<link href="https://fonts.googleapis.com/css2?family=EB+Garamond:wght@400;500;600&family=Montserrat:wght@400;500;600&family=Allura&display=swap" rel="stylesheet">
<style>
:root{
  --bg-light:#f4f5f7;
  --blue:#7e9fb4;
  --blue-text:#6f93aa;
  --slate:#66768a;
  --dark:#1d1e1a;
  --white:#ffffff;
  --ink:#3e4a55;
  --star:#e98a3c;
  --photo-a:#c9d8e3;
  --photo-b:#8fa9bc;
}
*{margin:0;padding:0;box-sizing:border-box}
html,body{width:1200px;height:4911px;overflow:hidden}
body{font-family:"EB Garamond",Georgia,serif;color:var(--ink);background:var(--bg-light);position:relative}
.section{position:absolute;left:0;width:1200px;overflow:hidden}
.abs{position:absolute}
.script{font-family:"Allura",cursive;font-weight:400}
.sans{font-family:"Montserrat",Arial,sans-serif}
.eyebrow{font-family:"EB Garamond",serif;font-size:14px;letter-spacing:3.5px;font-weight:500;text-transform:uppercase}
.btn{position:absolute;font-family:"Montserrat",sans-serif;font-size:15px;display:flex;align-items:center;justify-content:center;border-radius:4px}
.photo{position:absolute}

/* hero */
.hero{top:0;height:765px;background:var(--bg-light)}
.nav a{font-family:"Montserrat",sans-serif;font-size:16px;color:var(--blue-text);text-decoration:none;margin-right:22px}
.hero h1{font-size:64px;line-height:62px;font-weight:500;color:var(--blue-text)}
.hero h1 .script{font-size:76px}
.hero p{font-size:14.5px;line-height:23px;color:var(--ink)}

/* expertise */
.expertise{top:765px;height:748px;background:var(--blue);color:var(--white)}
.expertise h2{font-size:50px;line-height:62px;font-weight:500}
.expertise h2 .script{font-size:64px}
.expertise p{font-size:14.5px;line-height:23.5px}

/* offer */
.offer{top:1513px;height:880px;background:var(--slate);color:var(--white);text-align:center}
.offer h2{font-size:50px;font-weight:500}
.offer h2 .script{font-size:66px}
.offer-col{position:absolute;width:330px;text-align:center}
.offer-col h3{font-size:33px;font-weight:400;margin-top:0}
.offer-col p{font-size:14.5px;line-height:23.5px;font-weight:600;margin-top:14px}

/* testimonials */
.testimonials{top:2393px;height:780px;background:var(--bg-light);text-align:center}
.testimonials h2{font-size:52px;font-weight:500;color:var(--blue-text)}
.testimonials h2 .script{font-size:64px}
.quote-card{position:absolute;left:245px;top:249px;width:740px;height:371px;border:1px solid #dfe3e8;background:#f6f7f9}
.quote{font-family:"Montserrat",sans-serif;font-size:17px;letter-spacing:1.2px;line-height:20.5px;color:var(--ink)}

/* blog */
.blog{top:3173px;height:859px;background:var(--blue);color:var(--white)}
.blog h2{font-size:56px;font-weight:500;text-align:center}
.blog h2 .script{font-size:70px}
.post{position:absolute;width:302px;top:237px}
.post h3{font-size:26px;line-height:29px;font-weight:600;margin-top:18px}
.post p{font-size:14px;line-height:23.5px;margin-top:22px}

/* contact */
.contact{top:4032px;height:677px;background:var(--slate);color:var(--white)}
.contact h2{font-size:48px;font-weight:600;line-height:56px}
.contact h2 .script{font-size:64px;font-weight:400}
.contact p{font-size:14px;line-height:23.5px}

/* footer */
.footer{top:4709px;height:202px;background:var(--dark);color:var(--white);text-align:center}
</style>
</head>
<body>

<!-- HERO -->
<section class="section hero">
  <nav class="nav abs" style="left:100px;top:116px">
    <a href="#">Home</a><a href="#">Leistungen</a><a href="#">Über mich</a><a href="#">Blog</a>
  </nav>
  <div class="abs" style="left:520px;top:52px;width:160px;height:160px;display:flex;flex-direction:column;align-items:center;justify-content:center">
    <svg width="22" height="22" viewBox="0 0 22 22"><circle cx="11" cy="11" r="9" fill="none" stroke="#6f93aa" stroke-width="1.5"/></svg>
    <span style="font-size:16px;color:var(--blue-text);margin-top:6px;letter-spacing:1px">Lindholm Coaching</span>
  </div>
  <svg class="abs" style="left:840px;top:110px" width="150" height="32" viewBox="0 0 150 32" role="img" aria-label="Social-Media-Verweise">
    <circle cx="16" cy="16" r="14" fill="#7e9fb4"/>
    <circle cx="70" cy="16" r="14" fill="#7e9fb4"/>
    <circle cx="124" cy="16" r="14" fill="#7e9fb4"/>
  </svg>
  <div class="btn" style="left:1003px;top:111px;width:97px;height:32px;background:var(--blue);color:#fff;font-size:15px">Kontakt</div>

  <div class="photo" role="img" aria-label="Porträtfoto des Coaches mit verschränkten Armen, hellblaues Hemd" style="left:700px;top:230px;width:500px;height:535px;background:linear-gradient(160deg,var(--bg-light) 10%,var(--photo-a) 50%,var(--photo-b) 100%)"></div>

  <div class="eyebrow abs" style="left:100px;top:292px;color:var(--ink)">Für technische Visionäre</div>
  <h1 class="abs" style="left:98px;top:328px">Coaching,<br>das Sie zum <span class="script">Erfolg</span> führt</h1>
  <p class="abs" style="left:100px;top:490px;width:580px">Beratung für Führungskräfte und Entscheider mit technischem Hintergrund.<br>Mit einer fundierten Expertise in den Bereichen Forschung &amp; Entwicklung, Engineering, Technik, Maschinenbau und Naturwissenschaften stehe ich Ihnen zur Seite, um Ihre beruflichen und persönlichen Herausforderungen zu meistern.</p>
  <div class="btn" style="left:100px;top:608px;width:272px;height:44px;background:var(--blue);color:#fff;box-shadow:0 2px 4px rgba(0,0,0,.15)">Mehr über mein Angebot</div>
  <div class="btn" style="left:387px;top:608px;width:223px;height:44px;border:1.5px solid var(--blue);color:var(--blue-text);background:#fff">Termin vereinbaren</div>
</section>

<!-- EXPERTISE -->
<section class="section expertise">
  <div class="photo" role="img" aria-label="Porträtfoto des Coaches, nachdenkend mit Hand am Kinn" style="left:174px;top:210px;width:320px;height:320px;border-radius:50%;background:radial-gradient(circle at 50% 40%,#dfe7ee,#a9bfcf 70%,#8aa3b6)"></div>
  <div class="eyebrow abs" style="left:535px;top:112px">Matthias Lindholm</div>
  <h2 class="abs" style="left:535px;top:140px">Profitieren Sie von<br>meiner <span class="script">Expertise</span></h2>
  <p class="abs" style="left:535px;top:287px;width:520px">Ich bin Matthias Lindholm, zertifizierter Coach mit einer Leidenschaft für die Entwicklung von Führungskräften und Entscheidern im technischen Bereich. Mit einem Hintergrund in [Fachgebiet] und einer langjährigen Erfahrung in der Unterstützung von Menschen auf ihrem Weg zu persönlichem und beruflichem Wachstum, stehe ich Ihnen als vertrauensvoller Begleiter zur Seite.</p>
  <p class="abs" style="left:535px;top:427px;width:520px">Mein Coaching-Ansatz vereint technische Expertise mit einem tiefen Verständnis für persönliche Entwicklung und Sinnhaftigkeit in der Führung. In unserer Zusammenarbeit schaffen wir einen Raum für Reflexion, Sparring und zielgerichtete Veränderung. Meine Mission ist es, Sie dabei zu unterstützen, nicht nur beruflichen Erfolg zu erzielen, sondern auch eine erfüllende und sinnvolle Führungskraft zu werden.</p>
  <div class="btn" style="left:535px;top:592px;width:238px;height:42px;background:#fff;color:var(--ink)">Mehr Infos über mich</div>
  <div class="btn" style="left:788px;top:592px;width:178px;height:42px;border:1.5px solid #fff;color:#fff">Mein Angebot</div>
</section>

<!-- OFFER -->
<section class="section offer">
  <div class="eyebrow abs" style="left:0;width:1200px;top:116px">Mein Angebot</div>
  <h2 class="abs" style="left:0;width:1200px;top:140px"><span class="script">Gemeinsam</span> gehen wir auf Kurs</h2>

  <div class="photo" role="img" aria-label="Illustration: Coach und Klientin im Gespräch" style="left:118px;top:250px;width:282px;height:220px;border-radius:46% 54% 40% 60%/55% 45% 55% 45%;background:#7d8ea2"></div>
  <div class="photo" role="img" aria-label="Illustration: Zielscheibe mit Pfeilen" style="left:465px;top:250px;width:268px;height:220px;border-radius:50%;background:linear-gradient(135deg,#7a8a9e,#8c9aac)"></div>
  <div class="photo" role="img" aria-label="Illustration: Zahnräder mit arbeitender Person" style="left:815px;top:250px;width:250px;height:220px;border-radius:55% 45% 50% 50%/50% 55% 45% 50%;background:#7d8ea2"></div>

  <div class="offer-col" style="left:95px;top:496px"><h3>Coaching</h3><p>In meinem Coaching legen wir gemeinsam den Fokus auf bedeutungsvolle Veränderungen in Ihrem Leben und Ihrer beruflichen Laufbahn. Ich unterstütze Sie in den Bereichen Sinn-Coaching, begleite Sie durch Umbrüche und Veränderungen – sei es im privaten oder beruflichen Kontext – und biete Ihnen Sparring und Reflexion auf höchstem Niveau.</p></div>
  <div class="offer-col" style="left:438px;top:496px"><h3>Ihr Nutzen</h3><p>Als erfahrener Coach verbinde ich Fachkompetenz mit Einfühlungsvermögen, um Ihnen nicht nur praktische Werkzeuge an die Hand zu geben, sondern auch einen Raum für persönliches Wachstum und Entfaltung zu schaffen. Ihr Erfolg und Ihre Zufriedenheit stehen im Mittelpunkt meiner Arbeit.</p></div>
  <div class="offer-col" style="left:775px;top:496px"><h3>Zielgruppe</h3><p>Meine Dienstleistungen richten sich an Führungskräfte und Entscheider in technischen Disziplinen. Ob Sie in der Forschung tätig sind, im Bereich Engineering, Technik, Maschinenbau oder Naturwissenschaften – ich bin hier, um Sie auf Ihrem Weg zu begleiten.</p></div>
</section>

<!-- TESTIMONIALS -->
<section class="section testimonials">
  <div class="eyebrow abs" style="left:0;width:1200px;top:110px;color:var(--ink)">Testimonials</div>
  <h2 class="abs" style="left:0;width:1200px;top:135px">Echte Geschichten, echte <span class="script">Erfahrungen</span></h2>
  <div class="quote-card">
    <svg class="abs" style="left:262px;top:46px" width="216" height="36" viewBox="0 0 216 36">
      <g fill="#e98a3c">
        <polygon points="18,2 22.5,13 34,13.5 25,21 28,33 18,26.5 8,33 11,21 2,13.5 13.5,13"/>
        <polygon transform="translate(45 0)" points="18,2 22.5,13 34,13.5 25,21 28,33 18,26.5 8,33 11,21 2,13.5 13.5,13"/>
        <polygon transform="translate(90 0)" points="18,2 22.5,13 34,13.5 25,21 28,33 18,26.5 8,33 11,21 2,13.5 13.5,13"/>
        <polygon transform="translate(135 0)" points="18,2 22.5,13 34,13.5 25,21 28,33 18,26.5 8,33 11,21 2,13.5 13.5,13"/>
        <polygon transform="translate(180 0)" points="18,2 22.5,13 34,13.5 25,21 28,33 18,26.5 8,33 11,21 2,13.5 13.5,13"/>
      </g>
    </svg>
    <p class="quote abs" style="left:60px;top:117px;width:620px">"Als technische Führungskraft stand ich vor großen Herausforderungen bei der Umsetzung von Veränderungen in unserem Team. Herr Lindholm hat mir durch sein einfühlsames Coaching geholfen, nicht nur strategische Lösungen zu finden, sondern auch meine persönliche Führungskompetenz zu stärken."</p>
    <div class="photo" role="img" aria-label="Kundenporträt" style="left:225px;top:276px;width:60px;height:60px;border-radius:50%;background:radial-gradient(circle,#b7a99a,#6b6a5c)"></div>
    <div class="sans abs" style="left:309px;top:280px;font-size:17px;font-weight:600;color:var(--ink)">Stefan Brenner</div>
    <div class="sans abs" style="left:309px;top:307px;font-size:13px;color:#b6bec6">Norwerk AG</div>
  </div>
  <svg class="abs" style="left:170px;top:408px" width="34" height="56" viewBox="0 0 34 56"><polyline points="28,4 6,28 28,52" fill="none" stroke="#d3d9df" stroke-width="5"/></svg>
  <svg class="abs" style="left:1050px;top:408px" width="34" height="56" viewBox="0 0 34 56"><polyline points="6,4 28,28 6,52" fill="none" stroke="#5e6b78" stroke-width="5"/></svg>
  <svg class="abs" style="left:600px;top:652px" width="12" height="12"><circle cx="6" cy="6" r="5" fill="#1d1e1a"/></svg>
</section>

<!-- BLOG -->
<section class="section blog">
  <div class="eyebrow abs" style="left:0;width:1200px;top:112px;text-align:center">Blog</div>
  <h2 class="abs" style="left:0;width:1200px;top:132px">Reflexionen &amp; <span class="script">Erfolgsgeschichten</span></h2>

  <article class="post" style="left:112px">
    <div role="img" aria-label="Foto: Mann am Fenster in Gedanken" style="width:302px;height:170px;background:linear-gradient(120deg,#dde5ea,#7f8c94 60%,#3f4a52)"></div>
    <h3>Selbstreflexion für Führungskräfte - Kunst und Praxis</h3>
    <p>Tauchen Sie ein in die Kunst der Selbstreflexion und entdecken Sie, warum diese Fähigkeit für technische Führungskräfte so entscheidend ist. Finden Sie praktische Tipps, um diese in Ihrem Führungsalltag zu integrieren.</p>
  </article>
  <article class="post" style="left:450px">
    <div role="img" aria-label="Foto: Team feiert eine Idee" style="width:302px;height:170px;background:linear-gradient(120deg,#cfdbe4,#8ea6b8 50%,#e7d9a8)"></div>
    <h3>Innovation und Führung: Kreativität im Management</h3>
    <p>Entdecken Sie, wie Sie Kreativität im technischen Management fördern können: Bewährte Methoden, um eine inspirierende Unternehmenskultur zu schaffen und Innovationen in Ihrem Team zu fördern.</p>
  </article>
  <article class="post" style="left:788px">
    <div role="img" aria-label="Foto: zwei Geschäftsleute mit Boxhandschuhen" style="width:302px;height:170px;background:linear-gradient(120deg,#e4e6e8,#6e737a 55%,#3b3f45)"></div>
    <h3>Die Macht des Sparrings: Führung per konstruktivem Feedback</h3>
    <p>Erfahren Sie, wie Führungskräfte im technischen Bereich durch Sparring wachsen können. Lesen Sie praktische Einblicke, um Ihre Kompetenzen zu verbessern.</p>
  </article>

  <div class="btn" style="left:485px;top:702px;width:230px;height:40px;background:#fff;color:var(--ink)">Alle Artikel anzeigen</div>
</section>

<!-- CONTACT -->
<section class="section contact">
  <div class="eyebrow abs" style="left:140px;top:110px">Bereit für Veränderung?</div>
  <h2 class="abs" style="left:138px;top:140px">Ich bin für Sie da.<br><span class="script">Schreiben Sie mir!</span></h2>
  <p class="abs" style="left:140px;top:290px;width:520px">Vereinbaren Sie noch heute Ihr erstes kostenloses Beratungsgespräch und entdecken Sie, wie Coaching Ihr Leben und Ihre berufliche Laufbahn transformieren kann.</p>
  <p class="abs" style="left:140px;top:408px;width:520px">Wenn Sie nach einem engagierten Coach suchen, der Sie in Ihren Zielen unterstützt und Ihnen hilft, Ihr volles Potenzial zu entfalten, nehmen Sie Kontakt auf. Gemeinsam gestalten wir Ihren Weg zu nachhaltigem Erfolg und persönlichem Wohlbefinden.</p>
  <div class="btn" style="left:140px;top:508px;width:227px;height:40px;background:#fff;color:var(--ink)">Kontakt aufnehmen</div>
  <div class="photo" role="img" aria-label="Porträtfoto des Coaches, stehend mit verschränkten Armen" style="left:720px;top:135px;width:336px;height:336px;border-radius:50%;background:radial-gradient(circle at 50% 40%,#eef1f3,#b9c9d6 70%,#93aabc)"></div>
  <div class="abs" style="left:720px;width:336px;top:498px;text-align:center;font-size:16px;font-weight:600">Matthias Lindholm</div>
</section>

<!-- FOOTER -->
<footer class="section footer">
  <div class="abs" style="left:0;width:1200px;top:48px;font-size:24px;letter-spacing:4px">LINDHOLM COACHING</div>
  <div class="sans abs" style="left:0;width:1200px;top:100px;font-size:16px;font-weight:600">Impressum&nbsp;&nbsp;&nbsp;Datenschutz</div>
  <div class="sans abs" style="left:0;width:1200px;top:150px;font-size:13px">© 2024 Matthias Lindholm Coaching</div>
</footer>

</body>
</html>
```